Marrowby Nature Alliance needs a fundraiser poster

We are having an annual awards night and fundraiser.

On the top of the poster please put "Marrowby Nature Alliance Annual Awards Night and Fundraiser"

Date: March 25, 2023
Time: 6:00pm doors open. Supper at 7:00pm
Location: Quenford Sportsdome Auditorium
Cost: $40 for Adults, $20 for 18 and under

We also would like on the poster, "Live Auctions, Silent auctions, and raffles"
"Serving Elk, Moose, and Wild Boar. Also beef"

```html
<!DOCTYPE html>
<html lang="en">
<head>
<meta charset="utf-8">
<title>Marrowby Nature Alliance Annual Awards Night and Fundraiser</title>
<link rel="stylesheet" href="https://fonts.googleapis.com/css2?family=Bebas+Neue&family=Fira+Sans:wght@400;500;700&display=swap">
<style>
  :root {
    --backdrop: #b3b3b3;
    --bark: #2a1e16;
    --bark-deep: #1f1610;
    --taupe: #8d7868;
    --taupe-light: #bcaa9b;
    --gold: #f6c862;
    --gold-pale: #fde7a6;
    --amber: #e98a1b;
    --white: #ffffff;
    --ink: #1c140e;
    --rule: #6f5a3c;
  }
  html, body {
    margin: 0;
    width: 1200px;
    height: 1177px;
    overflow: hidden;
    background: var(--backdrop);
  }
  .poster {
    position: absolute;
    left: 248px;
    top: 126px;
    width: 728px;
    height: 940px;
    background: var(--bark);
    overflow: hidden;
    font-family: "Fira Sans", Arial, sans-serif;
    color: var(--white);
  }
  .hero-photo {
    position: absolute;
    left: 0; top: 0;
    width: 728px; height: 460px;
    background:
      radial-gradient(ellipse 220px 160px at 600px 40px, rgba(255,236,160,0.95), rgba(255,190,70,0) 70%),
      linear-gradient(180deg, #f3b54a 0%, #e79a2d 30%, #b8763a 52%, #7a5436 68%, #4a3424 84%, var(--bark) 100%);
  }
  .date-box {
    position: absolute;
    left: 559px; top: 229px;
    width: 118px; height: 210px;
    border: 2px solid var(--white);
    box-sizing: border-box;
    text-align: center;
    font-family: "Bebas Neue", "Oswald", sans-serif;
  }
  .date-day { font-size: 116px; line-height: 1; margin-top: 14px; color: var(--gold); }
  .date-month { font-size: 40px; line-height: 1; color: var(--white); margin-top: -4px; }
  .date-year { font-size: 43px; line-height: 1; color: var(--white); margin-top: 2px; }
  .headline {
    margin: 0;
    font-family: "Bebas Neue", "Oswald", sans-serif;
    font-weight: 400;
  }
  .headline-top, .headline-main {
    position: absolute;
    left: 60px;
    width: 619px;
    white-space: nowrap;
    line-height: 1;
  }
  .headline-top {
    top: 457px;
    font-size: 88px;
    color: var(--white);
  }
  .headline-main {
    top: 526px;
    font-size: 140px;
    background: linear-gradient(90deg, var(--gold-pale) 0%, var(--gold) 30%, var(--amber) 55%, var(--gold) 80%, var(--gold-pale) 100%);
    -webkit-background-clip: text;
    background-clip: text;
    color: transparent;
  }
  .location-bar {
    position: absolute;
    left: 60px; top: 660px;
    width: 619px; height: 54px;
    background: var(--taupe);
    display: flex;
    align-items: center;
  }
  .location-label {
    margin-left: 13px;
    width: 174px; height: 38px;
    background: var(--bark-deep);
    color: var(--amber);
    font-weight: 700;
    font-size: 22px;
    display: flex; align-items: center; justify-content: center;
    letter-spacing: 0.5px;
  }
  .location-name {
    flex: 1;
    text-align: center;
    font-weight: 700;
    font-size: 22px;
    white-space: nowrap;
  }
  .brand {
    position: absolute;
    left: 50px; top: 750px;
    width: 200px;
    text-align: center;
  }
  .brand-mark {
    width: 44px; height: 44px;
    border-radius: 50%;
    background: var(--white);
    margin: 0 auto 14px;
  }
  .brand-name {
    font-weight: 700;
    font-size: 22px;
    line-height: 1.15;
    color: var(--white);
  }
  .details {
    position: absolute;
    left: 268px; top: 723px;
    width: 400px;
    margin: 0; padding: 0;
    list-style: none;
    text-align: center;
  }
  .details li {
    height: 34px;
    line-height: 34px;
    box-sizing: border-box;
    border-bottom: 1px solid var(--rule);
    font-size: 16px;
    white-space: nowrap;
  }
  .details li:last-child { border-bottom: none; }
  .details .time { font-weight: 700; font-size: 17px; }
  .cost-box {
    position: absolute;
    left: 266px; top: 835px;
    width: 400px; height: 71px;
    background: var(--white);
    display: flex;
    align-items: center;
    color: var(--ink);
  }
  .cost-label {
    margin-left: 10px;
    width: 100px; height: 54px;
    background: var(--taupe-light);
    font-family: "Bebas Neue", "Oswald", sans-serif;
    font-size: 36px;
    display: flex; align-items: center; justify-content: center;
  }
  .price {
    display: flex;
    align-items: center;
    margin-left: 14px;
  }
  .price-amount {
    width: 50px; height: 50px;
    border-radius: 50%;
    background: var(--bark-deep);
    color: var(--amber);
    font-weight: 700;
    font-size: 21px;
    display: flex; align-items: center; justify-content: center;
  }
  .price-note {
    margin-left: 8px;
    font-size: 16px;
    line-height: 1.1;
  }
</style>
</head>
<body>
  <main class="poster">
    <div class="hero-photo" role="img" aria-label="Photo of a stag standing in frosted grass at golden sunrise with trees behind"></div>

    <div class="date-box">
      <div class="date-day">25</div>
      <div class="date-month">MARCH</div>
      <div class="date-year">2023</div>
    </div>

    <h1 class="headline">
      <span class="headline-top">ANNUAL AWARDS NIGHT</span>
      <span class="headline-main">&amp; FUNDRAISER</span>
    </h1>

    <div class="location-bar">
      <div class="location-label">LOCATION</div>
      <div class="location-name">QUENFORD SPORTSDOME AUDITORIUM</div>
    </div>

    <div class="brand">
      <div class="brand-mark"></div>
      <div class="brand-name">Marrowby<br>Nature Alliance</div>
    </div>

    <ul class="details">
      <li class="time">TIME: 6:00PM DOORS OPEN. SUPPER AT 7:00PM</li>
      <li>Live Auctions, Silent auctions, and raffles</li>
      <li>Serving Elk, Moose, and Wild Boar. Also beef</li>
    </ul>

    <div class="cost-box">
      <div class="cost-label">COST</div>
      <div class="price">
        <div class="price-amount">$40</div>
        <div class="price-note">for<br>Adults</div>
      </div>
      <div class="price">
        <div class="price-amount">$20</div>
        <div class="price-note">for 18<br>and under</div>
      </div>
    </div>
  </main>
</body>
</html>
```